PL regenerative food process graphic design for posters

We are a Hawaii snorkel tour company who makes all of our cruises vegan food from scratch and have a family farm we use for composting & growing food products. We want a design showing our food recycling process. From the soil to the tree's fruit to cooking, to eating, to zero-waste trash can, to recycle, to compost pile. Representing the complete circle in the process. We want you to use a breadfruit or ulu tree for our tree. We want to express our companies commitment to being good stewards to Hawaii and our planet's environmental health.

Target Market(s)

tourists, families traveling

Industry/Entity Type

Eco-tourism

Font styles to use
Sans Serif

Colors
59FF00
82FF00
B8FF75
E3FFCB
F4FFEA
FFC000
F8CF3A
FAE287
FDF2CF
FEFAEE

Requirements
Must have
• Small Pine Lark logo on artwork showing ownership, Hand drawn artwork, with written explanation at each step of the process
Nice to have
• easy to understand artwork showing the process from farm to table and back again
Should not have
• stock images, graphics, photos

```html
<!DOCTYPE html>
<html lang="en">
<head>
<meta charset="utf-8">
<title>Pine Lark – Food Recycling Process</title>
<link rel="stylesheet" href="https://fonts.googleapis.com/css2?family=Montserrat:wght@800&family=Fira+Sans+Extra+Condensed:wght@400;700&display=swap">
<style>
  :root{
    --backdrop:#2b2b2b;
    --paper:#e6f0cc;
    --paper-light:#f4f9e6;
    --ink:#111111;
    --band:#7dc242;
    --band-shadow:#9a9a9a;
    --red:#ef5859;
    --orange:#fbae1b;
    --lime:#a8cc3a;
    --green:#2a7f3e;
    --sky:#45a6dd;
    --navy:#344a9d;
    --purple:#a6248a;
    --ring-yellow:#f5c518;
    --icon-fill:#e9e9e9;
    --white:#ffffff;
  }
  html,body{margin:0;padding:0;width:1200px;height:1200px;overflow:hidden;background:var(--backdrop);}
  .poster{display:block;position:absolute;left:171px;top:0;width:858px;height:1200px;}
  .brand-name{font-family:"Fira Sans Extra Condensed",sans-serif;font-weight:700;font-size:100px;fill:var(--ink);}
  .brand-tag{font-family:"Fira Sans Extra Condensed",sans-serif;font-weight:700;font-size:22px;letter-spacing:4px;fill:var(--ink);}
  .title{font-family:"Montserrat",sans-serif;font-weight:800;font-size:80px;fill:var(--ink);}
  .step-title{font-family:"Fira Sans Extra Condensed",sans-serif;font-weight:700;font-size:28px;fill:var(--white);}
  .step-body{font-family:"Fira Sans Extra Condensed",sans-serif;font-weight:400;font-size:13.5px;fill:var(--white);}
  .flow-arrow{fill:none;stroke:var(--white);stroke-width:3.5;}
  .flow-start{fill:none;stroke:var(--white);stroke-width:3;}
  .segment{stroke:var(--paper);stroke-width:16;stroke-linejoin:miter;}
  .icon-ring{stroke-width:9;}
  .icon-art{fill:var(--icon-fill);stroke:var(--white);stroke-width:5;}
</style>
</head>
<body>
<svg class="poster" viewBox="342 80 1265 1770" xmlns="http://www.w3.org/2000/svg">
  <defs>
    <radialGradient id="paper-glow" cx="50%" cy="62%" r="60%">
      <stop offset="0" stop-color="var(--paper-light)"/>
      <stop offset="1" stop-color="var(--paper)"/>
    </radialGradient>
    <radialGradient id="tree-tone" cx="50%" cy="45%" r="55%">
      <stop offset="0" stop-color="#9a9a9a"/>
      <stop offset="1" stop-color="#dcdcdc"/>
    </radialGradient>
    <marker id="chevron" viewBox="0 0 20 20" refX="14" refY="10" markerWidth="8" markerHeight="8" orient="auto" markerUnits="userSpaceOnUse">
      <path d="M4 2 L16 10 L4 18" fill="none" stroke="#ffffff" stroke-width="3.5"/>
    </marker>
  </defs>

  <rect x="342" y="80" width="1265" height="1770" fill="url(#paper-glow)"/>

  <g class="brand">
    <text class="brand-name" x="973" y="250" text-anchor="middle">Pine Lark</text>
    <text class="brand-tag" x="973" y="283" text-anchor="middle">BIG ISLAND OCEAN GUIDES</text>
  </g>

  <g class="title-band">
    <rect x="410" y="400" width="1138" height="105" fill="var(--band-shadow)"/>
    <rect x="404" y="394" width="1138" height="105" fill="var(--band)"/>
    <circle cx="436" cy="448" r="9" fill="var(--white)"/>
    <circle cx="1512" cy="448" r="9" fill="var(--white)"/>
    <text class="title" x="973" y="475" text-anchor="middle">Food Recycling Process</text>
  </g>

  <g class="wheel">
    <path class="segment" fill="var(--red)"    d="M720.2 644.7 A583 583 0 0 1 1225.8 644.7 L1103.1 899.7 A300 300 0 0 0 842.9 899.7 Z"/>
    <path class="segment" fill="var(--orange)" d="M1225.8 644.7 A583 583 0 0 1 1541.3 1039.8 L1265.4 1103 A300 300 0 0 0 1103.1 899.7 Z"/>
    <path class="segment" fill="var(--lime)"   d="M1541.3 1039.8 A583 583 0 0 1 1428.6 1533.7 L1207.5 1357.2 A300 300 0 0 0 1265.4 1103 Z"/>
    <path class="segment" fill="var(--green)"  d="M1428.6 1533.7 A583 583 0 0 1 973 1753 L973 1470 A300 300 0 0 0 1207.5 1357.2 Z"/>
    <path class="segment" fill="var(--sky)"    d="M973 1753 A583 583 0 0 1 517.4 1533.7 L738.5 1357.2 A300 300 0 0 0 973 1470 Z"/>
    <path class="segment" fill="var(--navy)"   d="M517.4 1533.7 A583 583 0 0 1 404.7 1039.8 L680.6 1103 A300 300 0 0 0 738.5 1357.2 Z"/>
    <path class="segment" fill="var(--purple)" d="M404.7 1039.8 A583 583 0 0 1 720.2 644.7 L842.9 899.7 A300 300 0 0 0 680.6 1103 Z"/>
  </g>

  <circle cx="973" cy="1170" r="327" fill="none" stroke="var(--white)" stroke-width="2" stroke-dasharray="9 7"/>

  <g class="centre">
    <circle cx="973" cy="1170" r="232" fill="none" stroke="#333333" stroke-width="2" stroke-dasharray="5 4"/>
    <circle cx="973" cy="1170" r="214" fill="var(--white)" stroke="var(--ring-yellow)" stroke-width="8"/>
    <circle cx="973" cy="1165" r="170" fill="url(#tree-tone)" role="img" aria-label="Hand-drawn breadfruit ulu tree with leafy canopy, fruit and spreading roots"/>
  </g>

  <g class="icons">
    <circle class="icon-ring" cx="973" cy="843" r="76" fill="var(--white)" stroke="var(--orange)"/>
    <circle class="icon-art" cx="973" cy="843" r="64" role="img" aria-label="Sack of rich soil with a red trowel"/>

    <circle class="icon-ring" cx="1228.5" cy="966" r="76" fill="var(--white)" stroke="var(--lime)"/>
    <circle class="icon-art" cx="1228.5" cy="966" r="64" role="img" aria-label="Sliced breadfruit with green leaves"/>

    <circle class="icon-ring" cx="1286" cy="1243" r="76" fill="var(--white)" stroke="var(--green)"/>
    <circle class="icon-art" cx="1286" cy="1243" r="64" role="img" aria-label="Orange mixing bowl with a whisk"/>

    <circle class="icon-ring" cx="1114.8" cy="1464.7" r="76" fill="var(--white)" stroke="var(--sky)"/>
    <circle class="icon-art" cx="1114.8" cy="1464.7" r="64" role="img" aria-label="Two guests enjoying food together"/>

    <circle class="icon-ring" cx="831.2" cy="1464.7" r="76" fill="var(--white)" stroke="var(--navy)"/>
    <circle class="icon-art" cx="831.2" cy="1464.7" r="64" role="img" aria-label="Person emptying scraps into a bin"/>

    <circle class="icon-ring" cx="660" cy="1243" r="76" fill="var(--white)" stroke="var(--purple)"/>
    <circle class="icon-art" cx="660" cy="1243" r="64" role="img" aria-label="Recycling bin with food scraps"/>

    <circle class="icon-ring" cx="720" cy="966" r="76" fill="var(--white)" stroke="var(--red)"/>
    <circle class="icon-art" cx="720" cy="966" r="64" role="img" aria-label="Wooden compost crate with a shovel"/>
  </g>

  <g class="flows">
    <path class="flow-arrow" marker-end="url(#chevron)" d="M1118 722 Q1190 735 1245 790"/>
    <circle class="flow-start" cx="1110" cy="720" r="7"/>
    <path class="flow-arrow" marker-end="url(#chevron)" d="M1410 999 Q1432 1070 1442 1138"/>
    <circle class="flow-start" cx="1408" cy="991" r="7"/>
    <path class="flow-arrow" marker-end="url(#chevron)" d="M1380 1408 Q1340 1470 1292 1520"/>
    <circle class="flow-start" cx="1385" cy="1401" r="7"/>
    <path class="flow-arrow" marker-end="url(#chevron)" d="M1037 1635 Q965 1640 893 1634"/>
    <circle class="flow-start" cx="1045" cy="1634" r="7"/>
    <path class="flow-arrow" marker-end="url(#chevron)" d="M655 1512 Q605 1455 566 1400"/>
    <circle class="flow-start" cx="660" cy="1518" r="7"/>
    <path class="flow-arrow" marker-end="url(#chevron)" d="M506 1140 Q512 1065 543 1000"/>
    <circle class="flow-start" cx="506" cy="1148" r="7"/>
    <path class="flow-arrow" marker-end="url(#chevron)" d="M705 785 Q765 735 835 716"/>
    <circle class="flow-start" cx="698" cy="790" r="7"/>
  </g>

  <g class="step step-dirt">
    <text class="step-title" x="972" y="652" text-anchor="middle">1. Dirt step</text>
    <text class="step-body" text-anchor="middle">
      <tspan x="972" y="681">Healthy soil, rich in nutrients and organic</tspan>
      <tspan x="972" y="695.5">matter, starts with how we treat our ʻāina.</tspan>
      <tspan x="972" y="710">Our family farm follows organic,</tspan>
      <tspan x="972" y="724.5">bio-dynamic, and Korean Natural Farming</tspan>
      <tspan x="972" y="739">practices, preparing the soil</tspan>
      <tspan x="972" y="753.5">for planting</tspan>
    </text>
  </g>

  <g class="step step-ulu">
    <text class="step-title" text-anchor="middle">
      <tspan x="1318" y="766">2. ʻUlu/</tspan>
      <tspan x="1318" y="791">breadfruit</tspan>
      <tspan x="1318" y="816">step</tspan>
    </text>
    <text class="step-body" text-anchor="middle">
      <tspan x="1372" y="843">The organic produce we serve</tspan>
      <tspan x="1372" y="857.5">is nutrient-dense and flavorful</tspan>
      <tspan x="1372" y="872">and features some traditional</tspan>
      <tspan x="1372" y="886.5">Hawaiian "canoe plants" -</tspan>
      <tspan x="1372" y="901">plants the first Hawaiians</tspan>
      <tspan x="1372" y="915.5">brought to Hawaiʻi from</tspan>
      <tspan x="1372" y="930">Polynesia for food -</tspan>
      <tspan x="1372" y="944.5">like ʻulu (breadfruit), ʻuala</tspan>
      <tspan x="1372" y="959">(purple sweet potato), and</tspan>
      <tspan x="1372" y="973.5">maiʻa (banana)</tspan>
    </text>
  </g>

  <g class="step step-mixing">
    <text class="step-title" text-anchor="middle">
      <tspan x="1449" y="1203">3. Mixing bowl</tspan>
      <tspan x="1449" y="1230">step</tspan>
    </text>
    <text class="step-body" text-anchor="middle">
      <tspan x="1450" y="1263">All food is prepared daily</tspan>
      <tspan x="1450" y="1277.5">from scratch in our 100%</tspan>
      <tspan x="1450" y="1292">plant-based kitchen with</tspan>
      <tspan x="1450" y="1306.5">taste and nutritional</tspan>
      <tspan x="1450" y="1321">content in mind, as well as</tspan>
      <tspan x="1450" y="1335.5">being cruelty-free towards</tspan>
      <tspan x="1450" y="1350">animals and the</tspan>
      <tspan x="1450" y="1364.5">environment</tspan>
    </text>
  </g>

  <g class="step step-eating">
    <text class="step-title" x="1178" y="1578" text-anchor="middle">4. People eating step</text>
    <text class="step-body" text-anchor="middle">
      <tspan x="1178" y="1608">Make memories of snorkeling in</tspan>
      <tspan x="1178" y="1622.5">beautiful Kealakekua and enjoy an</tspan>
      <tspan x="1178" y="1637">exclusive foodie experience</tspan>
      <tspan x="1178" y="1651.5">of healthful, plant-based cuisine as</tspan>
      <tspan x="1178" y="1666">you've never experienced before</tspan>
    </text>
  </g>

  <g class="step step-trash">
    <text class="step-title" x="760" y="1578" text-anchor="middle">5. Trash can step</text>
    <text class="step-body" text-anchor="middle">
      <tspan x="760" y="1608">Pine Lark snorkel</tspan>
      <tspan x="760" y="1622.5">tours are</tspan>
      <tspan x="760" y="1637">zero-waste and do</tspan>
      <tspan x="760" y="1651.5">not produce trash</tspan>
      <tspan x="760" y="1666">for the landfill</tspan>
    </text>
  </g>

  <g class="step step-recycle">
    <text class="step-title" x="498" y="1226" text-anchor="middle">6. Recycle step</text>
    <text class="step-body" text-anchor="middle">
      <tspan x="500" y="1257">We recycle all</tspan>
      <tspan x="500" y="1271.5">cardboard, cans, and</tspan>
      <tspan x="500" y="1286">bottles. Any leftover</tspan>
      <tspan x="500" y="1300.5">or waste products</tspan>
      <tspan x="500" y="1315">from our kitchen &amp;</tspan>
      <tspan x="500" y="1329.5">meals are collected</tspan>
      <tspan x="500" y="1344">for composting on</tspan>
      <tspan x="500" y="1358.5">our farm</tspan>
    </text>
  </g>

  <g class="step step-compost">
    <text class="step-title" text-anchor="middle">
      <tspan x="587" y="815">7. Compost</tspan>
      <tspan x="587" y="840">step</tspan>
    </text>
    <text class="step-body" text-anchor="middle">
      <tspan x="585" y="869">The organic materials</tspan>
      <tspan x="585" y="883.5">we collect break down</tspan>
      <tspan x="585" y="898">over time into</tspan>
      <tspan x="585" y="912.5">nutrient-rich compost</tspan>
      <tspan x="585" y="927">which we use</tspan>
      <tspan x="585" y="941.5">on our farm to grow</tspan>
      <tspan x="585" y="956">produce served on</tspan>
      <tspan x="585" y="970.5">our tours</tspan>
    </text>
  </g>
</svg>
</body>
</html>
```